Design a menu for health restaurant

A health food restaurant in Los Angeles is seeking menu design. Our foods are made from scratch using whole ingredients.
Name: Grubb Larder
Address: 1000 E 60th StLos Angeles, CA 90247
Website: www.GrubbLarder.example
We are looking for a clean and simple menu. Brand colors are white/tan, green and orange.

Please see attached excel with menu items and logo. We do not yet have prices.

Colors
f78f20
9bcb3c
ffffff
fff3d1

Requirements
Must have
• Easy to read.
Trifold menu design (front and back).
VEGAN, VEGETARIAN, GLUTEN FREE, CONTAINS NUTS symbols.
Logo.
Nice to have
• Incorporate brand colors, but still be easy to read.
We would like to use the Belco font (attached) if it works. If not we are open to a similar font that is easy to read.

Please see attached images.
We like the images and headers of OPTION 1. Would like something similar in trifold format.
We like the clean fonts of OPTION 2.

```html
<!DOCTYPE html>
<html lang="en">
<head>
<meta charset="utf-8">
<title>Grubb Larder — Menu</title>
<link href="https://fonts.googleapis.com/css2?family=Luckiest+Guy&family=Varela+Round&family=Mulish:wght@300;400&display=swap" rel="stylesheet">
<style>
  :root {
    --cream: #fff3d1;
    --orange: #f78f20;
    --green: #9bcb3c;
    --white: #ffffff;
    --ink: #1f1f1f;
    --ink-soft: #3a3a3a;
    --veg: #8cc63f;
    --vegan: #f78f20;
    --nuts: #a4402e;
    --gf: #1f8a3b;
  }
  * { box-sizing: border-box; margin: 0; padding: 0; }
  html, body { width: 1200px; height: 517px; overflow: hidden; }
  body { background: var(--cream); color: var(--ink); font-family: "Mulish", sans-serif; position: relative; }

  .section { position: absolute; width: 334px; }
  .section-bar {
    position: relative; height: 17px; background: var(--orange);
    border-bottom: 2px solid var(--green);
  }
  .section-title {
    position: absolute; left: 3px; top: 7px;
    font-family: "Luckiest Guy", sans-serif; font-size: 18px; line-height: 1;
    letter-spacing: 0.6px; color: var(--white);
    -webkit-text-stroke: 2.4px var(--ink); paint-order: stroke fill;
  }
  .items { list-style: none; margin-top: 12px; }
  .item { position: relative; margin-bottom: 7.5px; }
  .item-name {
    font-family: "Varela Round", sans-serif; font-size: 11px; line-height: 12px;
    color: var(--ink); padding-right: 50px;
  }
  .price {
    position: absolute; right: 0; top: 0;
    font-family: "Varela Round", sans-serif; font-size: 11px; line-height: 12px;
  }
  .item-desc {
    font-size: 6.3px; line-height: 7.9px; font-weight: 300; color: var(--ink-soft);
    max-width: 272px;
  }
  .tag {
    font-family: "Varela Round", sans-serif; font-size: 7px; font-weight: 700;
    letter-spacing: 0.3px; margin-left: 3px; vertical-align: 1px;
    color: var(--cream); -webkit-text-stroke: 0.6px currentColor;
  }
  .tag.veg { -webkit-text-stroke-color: var(--veg); }
  .tag.vegan { -webkit-text-stroke-color: var(--vegan); }
  .tag.nuts { -webkit-text-stroke-color: var(--nuts); }
  .tag.gf { -webkit-text-stroke-color: var(--gf); }
  .tag-note { font-family: "Mulish", sans-serif; font-size: 6.5px; color: var(--ink-soft); }

  .legend {
    position: absolute; left: 833px; top: 461px; width: 334px; height: 21px;
    background: var(--white); display: flex; align-items: center; justify-content: center; gap: 6px;
    font-family: "Varela Round", sans-serif; font-size: 10px; color: var(--ink);
  }
  .legend .tag { font-size: 10px; margin-left: 0; vertical-align: 0; -webkit-text-stroke-width: 0.8px; }
  .legend .dot { font-size: 8px; }
</style>
</head>
<body>

<section class="section" style="left:33px; top:33px;">
  <div class="section-bar"><h2 class="section-title">BREAKFAST</h2></div>
  <ul class="items">
    <li class="item"><p class="item-name">Pastries <span class="tag veg">VEG</span></p><span class="price">$0.00</span>
      <p class="item-desc">"Croissant (regular, almond, chocolate)<br>Blueberry Muffin<br>Superseed Cookie"</p></li>
    <li class="item"><p class="item-name">Parfait <span class="tag veg">VEG</span></p><span class="price">$0.00</span>
      <p class="item-desc">Fresh strawberries and blueberries on yogurt and muesli and topped with honey drizzle.</p></li>
    <li class="item"><p class="item-name">Avocado Super Toast <span class="tag vegan">V</span></p><span class="price">$0.00</span>
      <p class="item-desc">Avocado Mash, Tomato, Basil, Ground Flax, Hemp Seed, Chickpeas, and Moringa Powder<br>on Whole Wheat Bread.</p></li>
    <li class="item"><p class="item-name">Brunch Burger</p><span class="price">$0.00</span>
      <p class="item-desc">House seasoned beef burger topped with an over medium egg, red leaf lettuce, tomato, housemade pickles and Larder Sauce on a bun.</p></li>
    <li class="item"><p class="item-name">Breakfast Sammy <span class="tag vegan">V</span><span class="tag-note">*option</span></p><span class="price">$0.00</span>
      <p class="item-desc">Your choice of over medium egg or tofu steak with guacamole, tomato, and Larder sauce on an English muffin.</p></li>
    <li class="item"><p class="item-name">AM Burrito <span class="tag veg">VEG</span></p><span class="price">$0.00</span>
      <p class="item-desc">Scrambled eggs, onion, red bell pepper, black beans, housemade salsa, yogurt, and pepper jack cheese in a tortilla.</p></li>
  </ul>
</section>

<section class="section" style="left:33px; top:276px;">
  <div class="section-bar"><h2 class="section-title">SALADS</h2></div>
  <ul class="items">
    <li class="item"><p class="item-name">Avocado, Golden Beet, and Cranberry Salad <span class="tag veg">VEG</span><span class="tag gf">GF</span></p><span class="price">$0.00</span>
      <p class="item-desc">Gold beets, avocado, dried cranberries, watermelon radish, red kale, romaine, mixed greens, and pepitas served with Golden Buddha dressing.</p></li>
    <li class="item"><p class="item-name">Burrata Salad <span class="tag veg">VEG</span><span class="tag gf">GF</span></p><span class="price">$0.00</span>
      <p class="item-desc">Tomato, melon, shredded basil, balsamic glaze, fresh cracked pepper, and olive oil with burrata.</p></li>
    <li class="item"><p class="item-name">Mediterranean Salad <span class="tag veg">VEG</span><span class="tag gf">GF</span></p><span class="price">$0.00</span>
      <p class="item-desc">Cucumbers, Kalamata olives, cherry tomatoes, parsley, tricolor quinoa, hard-boiled egg, and hummus on mixed greens, romaine, and red cabbage with lemon-olive oil dressing.</p></li>
    <li class="item"><p class="item-name">Vegan Chef Salad <span class="tag veg">VEG</span><span class="tag gf">GF</span><span class="tag nuts">N</span></p><span class="price">$0.00</span>
      <p class="item-desc">Roasted potatoes and carrots, chickpeas, avocado, microgreens and walnuts on mixed greens, romaine, and red kale with vegan ranch.</p></li>
    <li class="item"><p class="item-name">Rancher's Salad <span class="tag veg">VEG</span><span class="tag gf">GF</span></p><span class="price">$0.00</span>
      <p class="item-desc">Tomato, red onion, hard boiled egg, avocado, feta cheese, microgreens, and grilled chicken on romaine with Ranch dressing.</p></li>
  </ul>
</section>

<section class="section" style="left:433px; top:33px;">
  <div class="section-bar"><h2 class="section-title">WRAPS</h2></div>
  <ul class="items">
    <li class="item"><p class="item-name">Rancher's Wrap</p><span class="price">$0.00</span>
      <p class="item-desc">Tomato, red onion, hard boiled egg, avocado, feta cheese, microgreens, romaine, grilled chicken and Ranch dressing in a grilled wrap.</p></li>
    <li class="item"><p class="item-name">Vegan Tuna Wrap <span class="tag vegan">V</span></p><span class="price">$0.00</span>
      <p class="item-desc">Vegan tuna, romaine, avocado, celery, shallot, and oregano with Herbalicious Sauce in a whole grain wrap.</p></li>
    <li class="item"><p class="item-name">Vegetarian Wrap <span class="tag veg">VEG</span></p><span class="price">$0.00</span>
      <p class="item-desc">Roasted chickpeas, romaine, avocado, red bell pepper, shaved carrots, cucumber, spinach, basil, black beans and feta with lemon-hummus in a sprouted 7-grain wrap.</p></li>
  </ul>
</section>

<section class="section" style="left:433px; top:171px;">
  <div class="section-bar"><h2 class="section-title">BURGERS N' SAMMIES</h2></div>
  <ul class="items">
    <li class="item"><p class="item-name">Air Fried Chicken Sammy</p><span class="price">$0.00</span>
      <p class="item-desc">Air fried chicken breast topped with red leaf lettuce, tomato, house made pickles and Larder Sauce on a bun served with choice of salad of fries.</p></li>
    <li class="item"><p class="item-name">Grilled Chicken Sammy</p><span class="price">$0.00</span>
      <p class="item-desc">Grilled chicken topped with guacamole, red leaf lettuce, tomato, house made pickles and Larder Sauce. Served with regular fries or side salad.</p></li>
    <li class="item"><p class="item-name">Classic Beef Burger</p><span class="price">$0.00</span>
      <p class="item-desc">House seasoned beef burger topped with red leaf lettuce, tomato, cheddar cheese, house made pickles and Larder Sauce on a bun served with choice of salad of fries.</p></li>
    <li class="item"><p class="item-name">Black Bean Pine Nut Burger <span class="tag vegan">V</span><span class="tag nuts">N</span></p><span class="price">$0.00</span>
      <p class="item-desc">House made black bean pine nut burger topped with red leaf lettuce, tomato, house made pickles and mustard aioli on a bun served with choice of salad of fries.</p></li>
    <li class="item"><p class="item-name">Salmon Burger</p><span class="price">$0.00</span>
      <p class="item-desc">House made salmon burger topped with red leaf lettuce, tomato, house made pickles and Larder yogurt on a bun served with choice of salad of fries.</p></li>
  </ul>
</section>

<section class="section" style="left:433px; top:379px;">
  <div class="section-bar"><h2 class="section-title">COMBOS</h2></div>
  <ul class="items">
    <li class="item"><p class="item-name">Soup + Salad</p><span class="price">$0.00</span>
      <p class="item-desc">Your choice of soup and side salad. - 16oz soup + 38oz salad</p></li>
    <li class="item"><p class="item-name">Avo Toast Combo</p><span class="price">$0.00</span>
      <p class="item-desc">Half avocado toast and your choice of soup. 16oz</p></li>
    <li class="item"><p class="item-name">Soup + Sammy</p><span class="price">$0.00</span>
      <p class="item-desc">Your choice of soup and sandwich. - 16oz soup + Sandwich</p></li>
  </ul>
</section>

<section class="section" style="left:833px; top:33px;">
  <div class="section-bar"><h2 class="section-title">BOWLS</h2></div>
  <ul class="items">
    <li class="item"><p class="item-name">Southwest Bowl <span class="tag gf">GF</span><span class="tag nuts">N</span></p><span class="price">$0.00</span>
      <p class="item-desc">Your choice of protein with corn, black beans, red onions, almonds and avocado over quinoa with lime hot sauce.</p></li>
    <li class="item"><p class="item-name">Chimi Bowl <span class="tag gf">GF</span></p><span class="price">$0.00</span>
      <p class="item-desc">Your choice of protein with red bell pepper, mushrooms, zucchini, squash, onion, cherry tomatoes and fresh herb chimichurri on wild and brown rice.</p></li>
    <li class="item"><p class="item-name">Soba Noodle Bowl</p><span class="price">$0.00</span>
      <p class="item-desc">Your choice of protein with spinach, snow peas, roasted carrots, red bell pepper, cilantro, sesame seeds and ginger lime sauce over soba noodles.</p></li>
    <li class="item"><p class="item-name">Hollywood Bowl <span class="tag gf">GF</span></p><span class="price">$0.00</span>
      <p class="item-desc">Your choice of protein with broccoli, roasted corn, cherry tomatoes, basil, pepitas, flax seeds and lemon juice on wild and brown rice.</p></li>
    <li class="item"><p class="item-name">Larder Bowl <span class="tag gf">GF</span></p><span class="price">$0.00</span>
      <p class="item-desc">Your choice of protein with roasted chickpeas and cauliflower, zesty fennel salad and citrus yogurt.</p></li>
    <li class="item"><p class="item-name">Buddha Bowl</p><span class="price">$0.00</span>
      <p class="item-desc">Your choice of protein with corn, red kale, sweet potatoes, red cabbage, parsley, oregano, hummus, and farro.</p></li>
    <li class="item"><p class="item-name">Chili Rice Bowl <span class="tag gf">GF</span></p><span class="price">$0.00</span>
      <p class="item-desc">Chicken, onions, bell peppers, jalapeños, black &amp; kidney beans, and tomato over brown rice.</p></li>
  </ul>
</section>

<section class="section" style="left:833px; top:303px;">
  <div class="section-bar"><h2 class="section-title">SOUPS</h2></div>
  <ul class="items">
    <li class="item"><p class="item-name">Chicken Noodle <span class="tag gf">GF</span></p><span class="price">$0.00</span>
      <p class="item-desc">Chicken, egg noodles, root vegetables, oregano &amp; peppercorns.</p></li>
    <li class="item"><p class="item-name">Larder Chili <span class="tag gf">GF</span></p><span class="price">$0.00</span>
      <p class="item-desc">Chicken, onions, bell peppers, jalapeños, black &amp; kidney beans, and tomato.</p></li>
    <li class="item"><p class="item-name">Seasonal Rotating <span class="tag vegan">V</span><span class="tag gf">GF</span><br>(Butternut Squash Soup V+, GF)</p><span class="price">$0.00</span>
      <p class="item-desc">Butternut squash blended with warm spices, and coconut milk.</p></li>
  </ul>
</section>

<div class="legend">
  <span><span class="tag veg">VEG</span>Vegetarian</span><span class="dot">•</span>
  <span><span class="tag vegan">V</span>Vegan</span><span class="dot">•</span>
  <span><span class="tag nuts">N</span>Contains Nuts</span><span class="dot">•</span>
  <span><span class="tag gf">GF</span>Gluten Free</span>
</div>

</body>
</html>
```